Spectacular Business Card Design for AI SAAS Plattform called Leapvine.ai

Hi Creators
I need an outstanding new Design for my business card.
I run an AI automated Saas Plattform Called Leapvine.ai

Front side:
Logo
Slogan: DIY Business Development & Social Media Management
Data:
Name: Markus Obelwinter - CEO / Founder
email: m.obelwinter@leapvine.ai
mobile: +43 699 82 37 415

Company name:
Leapvine FlexCo

Backside:

What we stand for Slogan:
Vertrauen in KI-Technologie, getragen von menschlicher Vision: Dein Sprung nach vorn!
+ a fancy design what captures our core competencies - AI automisations, Social Media Management, Business development
(dont know if its too much, but AI and social media should be )

pls find attached the logo and the old design

Industry/Entity Type

AI automations for marketing and business development

Contact Information for Business Card

Front side: Logo Slogan: DIY Business Development & Social Media Management Data: Name: Markus Obelwinter - CEO / Founder email: m.obelwinter@leapvine.ai mobile: +43 699 82 37 415 Company name: Leapvine FlexCo Backside: What we stand for Slogan: Vertrauen in KI-Technologie, getragen von menschlicher Vision: Dein Sprung nach vorn!

Font styles to use
Serif
Sans Serif

Requirements
Nice to have
• a fancy design on the backside, a fancy design what captures our core competencies - AI automisations, Social Media Management, Business development

```html
<!DOCTYPE html>
<html lang="de">
<head>
<meta charset="utf-8">
<title>Leapvine – Business Card</title>
<link href="https://fonts.googleapis.com/css2?family=Zilla+Slab:wght@500;600&family=Lato:wght@400;700&display=swap" rel="stylesheet">
<style>
  :root {
    --teal: #13829a;
    --teal-deep: #0a6f86;
    --teal-card: #0a8aa2;
    --orange: #ef8a2d;
    --ink: #2b2b2b;
    --white: #ffffff;
    --stage: #1a1a1a;
  }
  * { margin: 0; padding: 0; box-sizing: border-box; }
  html, body { width: 1200px; height: 1000px; overflow: hidden; background: var(--stage); }
  .canvas { position: relative; width: 1200px; height: 1000px; }

  .card { position: absolute; width: 708px; height: 404px; overflow: hidden; }
  .card-front { left: 88px; top: 70px; background: var(--white); }
  .card-back { left: 353px; top: 509px; background: linear-gradient(90deg, var(--teal-deep) 0%, var(--teal-card) 45%, var(--teal-card) 100%); }

  .brand { position: absolute; display: flex; align-items: center; gap: 8px; font-family: "Lato", sans-serif; font-weight: 700; }
  .brand-mark { width: 22px; height: 22px; background: var(--orange); }
  .front-brand { left: 26px; top: 76px; font-size: 28px; color: var(--teal); }

  .slogan { position: absolute; left: 0; width: 710px; top: 125px; text-align: center;
    font-family: "Zilla Slab", serif; font-weight: 500; font-size: 26px; line-height: 29px; z-index: 2; }
  .slogan .line-teal { color: var(--teal); display: block; }
  .slogan .line-orange { color: var(--orange); display: block; }
  .slogan .amp { color: var(--ink); }

  .person { position: absolute; left: 22px; top: 236px; }
  .person-name { font-family: "Zilla Slab", serif; font-weight: 500; font-size: 28px; color: var(--teal); line-height: 30px; }
  .person-role { font-family: "Lato", sans-serif; font-size: 19px; color: var(--teal); margin-top: 2px; margin-left: 3px; }

  .contacts { position: absolute; left: 24px; top: 307px; list-style: none; font-family: "Lato", sans-serif; font-size: 19px; color: var(--ink); }
  .contacts li { display: flex; align-items: center; gap: 14px; height: 26px; }
  .contacts svg { width: 16px; height: 16px; flex: none; }

  .social-cluster { position: absolute; left: 377px; top: 115px; width: 331px; height: 289px;
    clip-path: polygon(265px 0, 331px 0, 331px 289px, 0 289px, 40px 235px, 103px 185px, 190px 130px, 218px 60px);
    background: radial-gradient(circle at 75% 75%, #e84a3c 0%, #2f7fc1 40%, #3fb56b 70%, #f4c430 100%); }

  .back-visual { position: absolute; left: 0; top: 0; width: 290px; height: 404px;
    background: linear-gradient(160deg, #0c7f97 0%, #2aa0b8 40%, #e0b89a 55%, #ef8a2d 70%, #0a7c93 100%); opacity: .9; }

  .back-text { position: absolute; left: 250px; width: 458px; top: 70px; text-align: center; color: var(--white); }
  .back-headline { font-family: "Zilla Slab", serif; font-weight: 600; font-size: 25px; line-height: 27px; text-transform: uppercase; }
  .back-headline .leap { display: block; margin-top: 8px; }
  .competencies { font-family: "Lato", sans-serif; font-size: 16px; margin-top: 16px; line-height: 23px; }
  .competencies h2 { font-size: 16px; font-weight: 700; margin-bottom: 3px; }
  .competencies .dot { display: inline-block; width: 7px; height: 7px; border-radius: 50%; background: var(--orange); margin: 0 8px 2px; vertical-align: middle; }
  .back-brand { left: 395px; top: 300px; font-size: 20px; color: var(--white); }
  .back-brand .brand-mark { width: 20px; height: 20px; }
</style>
</head>
<body>
<div class="canvas">

  <section class="card card-front">
    <div class="brand front-brand"><span class="brand-mark"></span>Leapvine</div>

    <div class="social-cluster" role="img" aria-label="Cluster of colourful round social media icons"></div>

    <h1 class="slogan">
      <span class="line-teal">DIY BUSINESS DEVELOPMENT</span>
      <span class="line-orange"><span class="amp">&amp;</span> SOCIAL MEDIA MANAGEMENT</span>
    </h1>

    <div class="person">
      <div class="person-name">Markus Obelwinter</div>
      <div class="person-role">CEO / FOUNDER</div>
    </div>

    <ul class="contacts">
      <li>
        <svg viewBox="0 0 16 16"><path d="M3 1.5l3 .5 1 3-2 1.5c.8 1.8 2 3 3.8 3.8L10.3 8l3 1 .5 3-2 2C6 13.5 2.5 10 2 3.5z" fill="none" stroke="var(--orange)" stroke-width="1.6" stroke-linejoin="round"/></svg>
        +43 699 82 37 415
      </li>
      <li>
        <svg viewBox="0 0 16 16"><path d="M1 7.5L15 1l-4 14-3-5.5z" fill="var(--orange)"/></svg>
        m.obelwinter@leapvine.ai
      </li>
      <li>
        <svg viewBox="0 0 16 16"><g fill="none" stroke="var(--orange)" stroke-width="1.4"><circle cx="8" cy="8" r="6.5"/><ellipse cx="8" cy="8" rx="3" ry="6.5"/><path d="M1.5 8h13"/></g></svg>
        Leapvine FlexCo
      </li>
    </ul>
  </section>

  <section class="card card-back">
    <div class="back-visual" role="img" aria-label="Illustration of a businessman in a teal suit pointing at rising white and orange growth arrows"></div>

    <div class="back-text">
      <p class="back-headline">Vertrauen in KI-Technologie,<br>getragen von menschlicher<span class="leap">Dein Sprung nach vorn!</span></p>
      <div class="competencies">
        <h2>Core Competencies:</h2>
        <p>AI automisations<span class="dot"></span>Social Media Management</p>
        <p>Business Development</p>
      </div>
    </div>

    <div class="brand back-brand"><span class="brand-mark"></span>Leapvine</div>
  </section>

</div>
</body>
</html>
```